Experienced and Professional Marriage Celebrant

I need a web design for my services as a marriage celebrant in the Sydney area. I want people to have the impression I am a modern and professional marriage celebrant who can tailor a wedding ceremony and execute the ceremony with a high level of care and accommodate and adapt to any style of wedding and personalities of couples. I like a mint and pink and black theme and I am not sure whether to use the professional photos of me, might be too stiff! But would like to see ideas you can come up with. Happy to use other photos you might have

Reason: I have haven't been able to respond as quickly as I would have liked this last week to comments so extending a few days. Thanks

```html
<!DOCTYPE html>
<html lang="en">
<head>
<meta charset="utf-8">
<title>Mira Hollis — Marriage Celebrant</title>
<link href="https://fonts.googleapis.com/css2?family=Great+Vibes&family=Cinzel:wght@400;700&family=Open+Sans:wght@400;600&family=Cormorant+Garamond:ital,wght@0,700;1,400&display=swap" rel="stylesheet">
<style>
:root{
  --pink:#c9579f;
  --pink-deep:#b4478c;
  --pink-soft:#f6dcec;
  --pink-pale:#fbeef6;
  --cream:#f6f1ea;
  --ink:#1d1d1d;
  --grey:#8a8a8a;
  --white:#ffffff;
  --script:"Great Vibes",cursive;
  --title:"Cinzel",serif;
  --body:"Open Sans",sans-serif;
  --italic:"Cormorant Garamond",serif;
}
*{margin:0;padding:0;box-sizing:border-box}
html,body{width:1200px;height:2957px;overflow:hidden}
body{position:relative;background:var(--white);font-family:var(--body);color:var(--ink)}
.abs{position:absolute}

/* Hero */
.hero{left:0;top:0;width:1200px;height:584px;background:linear-gradient(90deg,#efe6da 0%,#f3ece3 40%,#f6f1ec 100%)}
.hero-photo{left:493px;top:0;width:707px;height:584px;background:radial-gradient(circle at 42% 55%,#f09a78 0,#f4c0a6 16%,#efe4dc 34%,#f7f3f1 60%,#e9e3de 100%)}
.brand{left:271px;top:42px;font-family:var(--script);font-size:62px;color:var(--ink);line-height:1}
.brand-sub{left:283px;top:128px;font-family:var(--title);font-size:16px;letter-spacing:3px;color:var(--ink)}
.portrait{left:308px;top:173px;width:162px;height:162px;border-radius:50%;background:linear-gradient(160deg,#6d4a5a,#b07aa2 55%,#3a2a33);border:4px solid var(--white)}
.hero-quote{left:259px;top:362px;width:300px;font-family:var(--italic);font-style:italic;font-size:25px;line-height:31px;color:var(--pink)}
.hero-rule{left:340px;top:486px;width:110px;height:2px;background:var(--ink)}
.nav{right:50px;top:0;display:flex;height:104px}
.nav a{display:flex;align-items:center;padding:0 16px;font-size:13px;letter-spacing:.5px;color:#555;text-decoration:none}
.nav a.active{background:var(--pink);color:var(--white);width:64px;justify-content:center;margin-right:12px;font-weight:600}

/* Section titles */
.section-title{left:0;width:1200px;text-align:center;font-family:var(--title);font-size:25px;letter-spacing:2px;line-height:35px;color:var(--ink)}
.divider{left:530px;width:140px;height:14px}

/* Services */
.services-band{left:0;top:722px;width:1200px;height:128px;background:var(--pink-pale)}
.couple{left:205px;top:706px;width:180px;height:290px;border-radius:6px;background:linear-gradient(180deg,#4a4a4a 0%,#2c2c2c 60%,#e8a9cf 100%)}
.services-text{left:394px;top:742px;width:566px;text-align:center;font-size:13px;line-height:18px;color:var(--pink)}
.tagline{left:440px;top:860px;width:560px;text-align:center;font-family:var(--script);font-size:42px;color:var(--ink)}
.tagline-sub{left:440px;top:912px;width:560px;text-align:center;font-family:var(--title);font-size:27px;letter-spacing:2px;color:var(--pink)}
.btn-more{left:628px;top:968px;width:94px;height:25px;background:var(--pink-deep);color:var(--white);font-family:var(--title);font-size:12px;font-weight:700;display:flex;align-items:center;justify-content:center}

/* Gallery */
.lead{left:0;width:1200px;text-align:center;font-size:13px;color:var(--pink)}
.gallery-band{left:0;top:1200px;width:1200px;height:407px;background:var(--cream)}
.frame{background:var(--white);border:6px solid var(--pink-soft);padding:8px;box-shadow:0 0 0 1px #e8b6d6}
.frame div{width:100%;height:100%}
.g1{left:128px;top:1239px;width:205px;height:294px}
.g1 div{background:linear-gradient(180deg,#4c84c4,#a9c5df 45%,#c8a4b8)}
.g2{left:377px;top:1239px;width:380px;height:294px}
.g2 div{background:linear-gradient(180deg,#2f66b8,#8fb3d8 50%,#b38a66 70%,#8c6a48)}
.g3{left:806px;top:1239px;width:217px;height:294px}
.g3 div{background:linear-gradient(180deg,#9ab3cc,#4a5560 55%,#e6e4e0)}
.dots{left:532px;top:1560px;display:flex;gap:10px}
.dots span{width:12px;height:12px;border-radius:50%;background:#d7d7d7}
.dots span.on{background:var(--pink)}

/* Testimonials */
.testimonial-band{left:0;top:1801px;width:1200px;height:256px;background:linear-gradient(90deg,#6b4a30,#b98a5c 30%,#f1d7b0 55%,#e3c9a8 75%,#8c6a4c)}
.quote-box{left:295px;top:1852px;width:696px;height:98px;background:rgba(255,255,255,.82)}
.quote-mark{left:206px;top:1822px;font-family:var(--italic);font-weight:700;font-size:170px;color:#f1aed4;line-height:1}
.quote-text{left:315px;top:1877px;width:656px;text-align:center;font-size:15px;line-height:22px;color:var(--pink)}
.quote-name{left:500px;top:1960px;width:380px;text-align:center;font-family:var(--script);font-size:28px;color:var(--pink)}
.quote-role{left:500px;top:1998px;width:380px;text-align:center;font-family:var(--title);font-size:13px;letter-spacing:3px;color:var(--ink)}
.arrow-left{left:152px;top:1888px}

/* Know */
.know-band{left:0;top:2230px;width:1200px;height:468px;background:var(--cream)}
.step-num{left:210px;font-family:var(--italic);font-style:italic;font-size:36px;color:var(--pink)}
.step-text{left:259px;width:470px;font-size:13px;line-height:18px;color:var(--pink)}
.step-rule{left:460px;width:60px;height:2px;background:#999}
.snap{background:var(--white);padding:10px;box-shadow:0 3px 10px rgba(0,0,0,.2)}
.snap div{width:100%;height:100%}
.snap-a{left:775px;top:2275px;width:220px;height:290px;transform:rotate(6deg);border:5px solid var(--pink-soft)}
.snap-a div{background:linear-gradient(160deg,#6a6f75,#d8d2cc 50%,#3f4246)}
.snap-b{left:900px;top:2420px;width:220px;height:200px;transform:rotate(-6deg);border:5px solid var(--pink-soft)}
.snap-b div{background:linear-gradient(180deg,#6f99c2,#b9c9d6 50%,#8a7a66)}

/* Footer */
.footer{left:0;top:2698px;width:1200px;height:227px;background:var(--pink-pale)}
.footer-brand{left:160px;top:2718px;font-family:var(--script);font-size:30px;color:var(--pink)}
.footer-menu{left:165px;top:2781px;list-style:none;font-size:11px;line-height:22px;color:#555}
.footer-head{font-size:11px;letter-spacing:1px;color:#555}
.socials{left:352px;top:2810px;display:flex;gap:6px}
.socials span{width:24px;height:24px;background:#9aa8d6}
.map-link{left:352px;top:2858px;display:flex;gap:8px;font-size:11px;line-height:15px;color:#555}
.field{background:var(--white);border:1px solid #e6c6da;font-size:10px;color:#888;padding:4px 6px}
.btn-submit{left:788px;top:2883px;width:259px;height:22px;background:var(--pink);color:var(--white);font-family:var(--title);font-size:11px;letter-spacing:2px;display:flex;align-items:center;justify-content:center}
.bottom-bar{left:0;top:2925px;width:1200px;height:32px;background:var(--pink);color:var(--white);font-size:15px;display:flex;align-items:center}
.bottom-bar span{position:absolute}
</style>
</head>
<body>

<header>
  <div class="abs hero"></div>
  <div class="abs hero-photo" role="img" aria-label="Bride in white holding a bouquet of peach and coral roses and lilies"></div>
  <div class="abs brand">Mira Hollis</div>
  <div class="abs brand-sub">MARRIAGE CELEBRANT</div>
  <div class="abs portrait" role="img" aria-label="Portrait of the celebrant"></div>
  <p class="abs hero-quote">Etiam id lectus eu nibh cursus blandit. Donec iaculis interdum sapien</p>
  <div class="abs hero-rule"></div>
  <nav class="abs nav">
    <a class="active" href="#">HOME</a>
    <a href="#">MY SERVICES</a>
    <a href="#">TESTIMONIALS</a>
    <a href="#">MARRIAGE</a>
    <a href="#">CONTACT</a>
  </nav>
</header>

<svg width="0" height="0" style="position:absolute">
  <symbol id="heart-divider" viewBox="0 0 140 14">
    <line x1="0" y1="7" x2="58" y2="7" stroke="#999" stroke-width="1"/>
    <line x1="82" y1="7" x2="140" y2="7" stroke="#999" stroke-width="1"/>
    <path d="M70 13 L63 6 A3.5 3.5 0 0 1 70 3 A3.5 3.5 0 0 1 77 6 Z" fill="#f08cc4"/>
  </symbol>
</svg>

<section class="services">
  <h2 class="abs section-title" style="top:637px">MY SERVICES</h2>
  <svg class="abs divider" style="top:680px"><use href="#heart-divider"/></svg>
  <div class="abs services-band"></div>
  <div class="abs couple" role="img" aria-label="Black silhouette of a bride and groom with a pink ribbon swirl"></div>
  <p class="abs services-text">Lorem ipsum dolor sit amet, consectetur adipiscing elit, sed do eiusmod tempor incididunt ut labore et dolore magna aliqua. Lorem ipsum dolor sit amet, consectetur adipiscing elit, sed do eiusmod tempor incididunt ut labore et dolore magna aliqua. Lorem ipsum dolor sit amet, consectetur adipiscing elit, sed do eiusmod tempor incididunt ut labore et dolore magna aliqua.</p>
  <p class="abs tagline">Dream it · Create it · Live it</p>
  <p class="abs tagline-sub">Your Perfect Wedding Day!</p>
  <a class="abs btn-more">MORE</a>
</section>

<section class="gallery">
  <h2 class="abs section-title" style="top:1082px">GALLERY</h2>
  <svg class="abs divider" style="top:1124px"><use href="#heart-divider"/></svg>
  <p class="abs lead" style="top:1164px">Lorem ipsum dolor sit amet, consectetur adipiscing elit</p>
  <div class="abs gallery-band"></div>
  <div class="abs frame g1"><div role="img" aria-label="Ceremony on a beach with bridesmaids"></div></div>
  <div class="abs frame g2"><div role="img" aria-label="Wedding party walking along the sand"></div></div>
  <div class="abs frame g3"><div role="img" aria-label="Couple standing by the water"></div></div>
  <div class="abs dots"><span></span><span></span><span class="on"></span><span></span><span></span></div>
</section>

<section class="testimonials">
  <h2 class="abs section-title" style="top:1670px">WHAT MY CLIENTS SAY<br>ABOUT ME</h2>
  <svg class="abs divider" style="top:1748px"><use href="#heart-divider"/></svg>
  <div class="abs testimonial-band" role="img" aria-label="Bride's gown and bouquet in warm evening light"></div>
  <svg class="abs arrow-left" width="20" height="40" viewBox="0 0 20 40"><polyline points="16,4 4,20 16,36" fill="none" stroke="#fff" stroke-width="2"/></svg>
  <div class="abs quote-box"></div>
  <div class="abs quote-mark">“</div>
  <p class="abs quote-text">Dolor sit amet, consectetur adipiscing elit, sed do eiusmod tempor incididunt ut labore et dolore magna aliqua.</p>
  <p class="abs quote-name">Lena Marsh</p>
  <p class="abs quote-role">BRIDE</p>
</section>

<section class="know">
  <h2 class="abs section-title" style="top:2118px">WHAT YOU NEED TO KNOW<br>WHEN GETTING MARRIED</h2>
  <svg class="abs divider" style="top:2198px"><use href="#heart-divider"/></svg>
  <div class="abs know-band"></div>
  <span class="abs step-num" style="top:2290px">1.</span>
  <p class="abs step-text" style="top:2302px">Lorem ipsum dolor sit amet, consectetur adipiscing elit, sed do eiusmod tempor incididunt ut labore et dolore magna aliqua. Lorem ipsum dolor sit amet, consectetur adipiscing elit, sed do eiusmod.</p>
  <div class="abs step-rule" style="top:2397px"></div>
  <span class="abs step-num" style="top:2426px">2.</span>
  <p class="abs step-text" style="top:2438px">Sit amet, consectetur adipiscing elit, sed do eiusmod tempor incididunt ut labore et dolore magna aliqua. Lorem ipsum dolor sit amet, consectetur adipiscing elit.</p>
  <div class="abs step-rule" style="top:2518px"></div>
  <span class="abs step-num" style="top:2549px">3.</span>
  <p class="abs step-text" style="top:2561px">Tempor incididunt ut labore et dolore magna aliqua. Lorem ipsum dolor sit amet, consectetur adipiscing elit, sed do eiusmod tempor incididunt ut labore et dolore magna aliqua. Lorem ipsum dolor.</p>
  <div class="abs snap snap-a"><div role="img" aria-label="Couple's hands with wedding rings"></div></div>
  <div class="abs snap snap-b"><div role="img" aria-label="Reception table set by the sea"></div></div>
</section>

<footer>
  <div class="abs footer"></div>
  <p class="abs footer-brand">Mira Hollis Celebrant</p>
  <ul class="abs footer-menu">
    <li>HOME</li><li>MY SERVICES</li><li>TESTIMONIALS</li><li>MARRIAGE</li><li>CONTACT</li>
  </ul>
  <p class="abs footer-head" style="left:352px;top:2784px">FOLLOW ME ON</p>
  <div class="abs socials"><span></span><span></span><span></span><span></span><span></span></div>
  <div class="abs map-link">
    <svg width="16" height="22" viewBox="0 0 16 22"><path d="M8 21 C3 14 1 11 1 8 A7 7 0 0 1 15 8 C15 11 13 14 8 21 Z" fill="#9aa8d6"/><circle cx="8" cy="8" r="2.5" fill="#fff"/></svg>
    <span>FIND ME ON<br>THE MAP</span>
  </div>
  <p class="abs footer-head" style="left:618px;top:2784px">GET IN TOUCH WITH ME</p>
  <div class="abs field" style="left:621px;top:2814px;width:155px;height:22px">Name*</div>
  <div class="abs field" style="left:621px;top:2846px;width:155px;height:22px">E-Mail*</div>
  <div class="abs field" style="left:788px;top:2814px;width:259px;height:57px"></div>
  <a class="abs btn-submit">SUBMIT YOUR MESSAGE</a>
  <div class="abs bottom-bar">
    <span style="left:259px">Phone: &nbsp; + 1 800 555 0142</span>
    <span style="left:640px">E-mail: &nbsp; mira.hollis.celebrant@example.com</span>
  </div>
</footer>

</body>
</html>
```